Web Design Project for Web Agency

WHAT I NEED:
The design I need (PSD file) is for a microsite designed for employee recruitment for Brennick, a Web agency.
***Design for the 1st Page ONLY : "Manifeste"
OBJECTIVES OF THE WEBSITE:
1. To promote the agency's corporate culture and HR management principles.
2. To get people to apply on available jobs
ELEMENTS OF THE PAGE "MANIFESTE" :
1. Brennick logo (see attached files). Beside the logo must be the word "Carrières" ("Careers" in english)
***The logo is not final and there is NO branding for Brennick yet. That is why there are multiple files. So please feel free to be creative!
2. Main menu : 4 sections
Manifeste | Opportunités | Brenick | Postuler
3. Manifeste :
This page is the home page. It will present 2 main sections :
a. The agency's corporate culture :
- Title of the page is a question : "Do you embrace Brennick's corporate culture?"
- Then, presentation of the 5 corporate values, each with a title and short description
- At the end of the list of values, we want a button that says "Apply now"
b. The agency's HR management principles :
- Title of the page is a question : "Do you see yourself working at Brennick?"
- Then, presentation of the 5 Management principles, each with a title and short description
- At the end of the list of principles, we want a button that says "Apply now"
VISUAL INSPIRATION
To create each section of the "Manifeste" page, we want a design that will fit with the corporate culture:
- Brennick is BOLD
- Brennick is PROUD
- Brennick is PROFESSIONAL
- Brennick is ELEGANT
- Brennick is REFINED
We want something slick and modern. Here are some Website's that we like that can be of inspiration:
- http://www.studio-varnel.com/en/services
- http://quillmorrowlab.com/

```html
<!DOCTYPE html>
<html lang="fr">
<head>
<meta charset="utf-8">
<title>Brennick Carrières – Manifeste</title>
<link rel="stylesheet" href="https://fonts.googleapis.com/css2?family=Montserrat:wght@600;700&family=Open+Sans:wght@400;600&display=swap">
<style>
  :root {
    --orange: #f47a36;
    --orange-deep: #e0661c;
    --amber: #f0b64e;
    --grey-text: #8e8e8e;
    --grey-logo: #b4b4b4;
    --rule: #dcdcdc;
    --body-text: #333333;
    --white: #ffffff;
    --photo-light: #d9d9d9;
    --photo-dark: #5a5a5a;
  }
  * { margin: 0; padding: 0; box-sizing: border-box; }
  html, body { width: 1200px; height: 1000px; overflow: hidden; background: var(--white); }
  .page { position: relative; width: 1200px; height: 1000px; font-family: "Open Sans", Arial, sans-serif; }

  .brand { position: absolute; left: 296px; top: 32px; }
  .brand-name { font-family: "Montserrat", Arial, sans-serif; font-weight: 700; font-size: 33px; color: var(--orange); line-height: 1; letter-spacing: -0.5px; }
  .brand-tagline { font-family: "Montserrat", Arial, sans-serif; font-weight: 600; font-size: 8px; letter-spacing: 2.6px; color: #555; margin-top: 6px; padding-left: 9px; }
  .brand-divider { position: absolute; left: 461px; top: 40px; width: 1px; height: 26px; background: var(--rule); }
  .brand-section { position: absolute; left: 472px; top: 44px; font-family: "Montserrat", Arial, sans-serif; font-weight: 700; font-size: 20px; color: var(--grey-logo); }

  .main-nav { position: absolute; right: 302px; top: 64px; display: flex; align-items: center; }
  .main-nav a { font-family: "Open Sans", Arial, sans-serif; font-weight: 600; font-size: 9.5px; color: var(--orange); text-decoration: none; letter-spacing: 0.3px; padding: 0 7px; border-left: 1px solid #f4c6a8; line-height: 11px; }
  .main-nav a:first-child { border-left: none; }
  .main-nav a:last-child { padding-right: 0; }

  .hero { position: absolute; left: 0; top: 102px; width: 1200px; height: 226px;
    background: linear-gradient(100deg, var(--orange-deep) 0%, #ec8a26 35%, #f0a03a 65%, var(--amber) 100%);
    box-shadow: inset 0 6px 8px -6px rgba(0,0,0,0.25); }
  .hero-title { position: absolute; left: 0; top: 52px; width: 1200px; text-align: center; font-family: "Montserrat", Arial, sans-serif; font-weight: 700; font-size: 32px; line-height: 37px; letter-spacing: 7px; color: var(--white); text-transform: uppercase; text-shadow: 1px 2px 3px rgba(0,0,0,0.35); }

  .section-heading { position: absolute; left: 302px; top: 360px; width: 603px; height: 14px; }
  .section-heading::before, .section-heading::after { content: ""; position: absolute; top: 5px; width: 162px; height: 1px; background: var(--rule); }
  .section-heading::before { left: 0; }
  .section-heading::after { right: 0; }
  .section-heading h2 { text-align: center; font-family: "Montserrat", Arial, sans-serif; font-weight: 700; font-size: 9px; letter-spacing: 2px; color: var(--orange); line-height: 12px; }

  .value { position: absolute; width: 180px; }
  .value-photo { display: block; width: 124px; height: 124px; border-radius: 50%; border: 4px solid var(--orange);
    background: radial-gradient(circle at 40% 40%, var(--photo-light) 0%, #a8a8a8 55%, var(--photo-dark) 100%); }
  .value-title { position: absolute; top: 143px; font-family: "Montserrat", Arial, sans-serif; font-weight: 700; font-size: 8.5px; letter-spacing: 0.3px; color: var(--grey-text); text-transform: uppercase; white-space: nowrap; }
  .value-text { position: absolute; top: 166px; left: 0; width: 180px; font-size: 10px; line-height: 17px; color: var(--body-text); }

  .apply { position: absolute; left: 302px; top: 925px; width: 598px; height: 31px; }
  .apply::before, .apply::after { content: ""; position: absolute; top: 16px; width: 196px; height: 1px; background: var(--rule); }
  .apply::before { left: 0; }
  .apply::after { right: 0; }
  .apply-button { position: absolute; left: 239px; top: 0; width: 120px; height: 31px; background: var(--orange); color: var(--white); font-family: "Montserrat", Arial, sans-serif; font-weight: 700; font-size: 9px; letter-spacing: 2px; text-decoration: none; display: flex; align-items: center; justify-content: center; }
</style>
</head>
<body>
<div class="page">
  <header>
    <div class="brand">
      <div class="brand-name">Brennick</div>
      <div class="brand-tagline">AGENCE NUMÉRIQUE</div>
    </div>
    <div class="brand-divider"></div>
    <div class="brand-section">Carrières</div>
    <nav class="main-nav">
      <a href="#">MANIFESTE</a>
      <a href="#">OPPORTUNITÉS</a>
      <a href="#">BRENICK</a>
      <a href="#">POSTULER</a>
    </nav>
  </header>

  <section class="hero" role="img" aria-label="Orange architectural grid backdrop">
    <h1 class="hero-title">Do you<br>embrace Brennick's<br>corporate culture?</h1>
  </section>

  <div class="section-heading"><h2>BRENNICK 5 CORPORATE VALUES</h2></div>

  <article class="value" style="left:302px; top:412px;">
    <span class="value-photo" style="margin-left:19px;" role="img" aria-label="Black and white photo of a handshake"></span>
    <h3 class="value-title" style="left:39px;">Brennick is bold</h3>
    <p class="value-text">Lorem ipsum dolor sit amet, consectetur adipiscing elit. Sed pellentesque, purus sit amet pulvinar sollicitudin, nulla odio hen-</p>
  </article>

  <article class="value" style="left:507px; top:412px;">
    <span class="value-photo" style="margin-left:30px;" role="img" aria-label="Black and white photo of people clapping"></span>
    <h3 class="value-title" style="left:44px;">Brennick is proud</h3>
    <p class="value-text">Lorem ipsum dolor sit amet, consectetur adipiscing elit. Sed pellentesque, purus sit amet pulvinar sollicitudin, nulla odio hen-</p>
  </article>

  <article class="value" style="left:722px; top:412px;">
    <span class="value-photo" style="margin-left:23px;" role="img" aria-label="Black and white photo of stacked team hands"></span>
    <h3 class="value-title" style="left:27px;">Brennick is professional</h3>
    <p class="value-text">Lorem ipsum dolor sit amet, consectetur adipiscing elit. Sed pellentesque, purus sit amet pulvinar sollicitudin, nulla odio hen-</p>
  </article>

  <article class="value" style="left:407px; top:661px;">
    <span class="value-photo" style="margin-left:31px;" role="img" aria-label="Black and white photo of a businessman adjusting his cuff"></span>
    <h3 class="value-title" style="left:45px;">Brennick is elegant</h3>
    <p class="value-text">Lorem ipsum dolor sit amet, consectetur adipiscing elit. Sed pellentesque, purus sit amet pulvinar sollicitudin, nulla odio hen-</p>
  </article>

  <article class="value" style="left:622px; top:661px;">
    <span class="value-photo" style="margin-left:25px;" role="img" aria-label="Black and white photo of a hand holding a business card"></span>
    <h3 class="value-title" style="left:28px;">Brennick is refined</h3>
    <p class="value-text">Lorem ipsum dolor sit amet, consectetur adipiscing elit. Sed pellentesque, purus sit amet pulvinar sollicitudin, nulla odio hen-</p>
  </article>

  <div class="apply"><a class="apply-button" href="#">APPLY NOW</a></div>
</div>
</body>
</html>
```